IT Company needs full suite of stationery

Our company 4027 Veltrane Partners Inc. is an IT company based in Toronto, Canada. Based on our logo we would like to see business cards(front and back), letterhead, envelope, brochure template. Design would be simple, not too bright, modern but can be used for many years, good theme throughout. Our official logo is the the fullcolor_a, full company name is 4027 Veltrane Partners Inc., Please include full company name on all pieces. Logo can be modified to be the graphic only with the "4027 Partners", I have cropped it myself for a couple files but I am no designer. We will provide lots of feedback so post early and often.
Updates

Reason: Very busy around the holidays, like a lot of the designs currently submitted, will definitely be picking one. Thanks for your submissions and merry Christmas and Happy New Year to everyone.

Industry/Entity Type

Business

```html
<!DOCTYPE html>
<html lang="en">
<head>
<meta charset="utf-8">
<title>4027 Partners — Trifold Brochure</title>
<link href="https://fonts.googleapis.com/css2?family=Exo+2:wght@300;400;500&family=Open+Sans:ital,wght@0,400;0,600;1,400;1,700&display=swap" rel="stylesheet">
<style>
  :root{
    --backdrop:#8a8c8f;
    --paper:#ffffff;
    --green:#2f9a4c;
    --green-light:#46b060;
    --green-deep:#1f6e36;
    --ink-dark:#1b2a1f;
    --charcoal:#3b3835;
    --charcoal-deep:#2a2826;
    --band-dark:#111111;
    --text-light:#ffffff;
    --text-muted:#6b6b6b;
    --heading-font:"Exo 2", sans-serif;
    --body-font:"Open Sans", sans-serif;
  }
  *{box-sizing:border-box;margin:0;padding:0}
  html,body{width:1200px;height:1000px;overflow:hidden}
  body{background:var(--backdrop);font-family:var(--body-font);position:relative}

  .brochure{position:absolute;left:60px;top:83px;width:1080px;height:834px;display:flex;
    box-shadow:0 10px 30px rgba(0,0,0,.25)}
  .panel{width:360px;height:834px;position:relative;overflow:hidden}

  /* Inside panel — green */
  .panel--feature{background:var(--paper);padding:18px}
  .feature-sheet{position:absolute;inset:18px;background:linear-gradient(160deg,var(--green-light),var(--green) 45%,var(--green-deep));}
  .feature-block{position:absolute;left:22px;right:22px}
  .feature-block--top{top:34px}
  .feature-block--bottom{top:508px}
  .feature-title{font-family:var(--heading-font);font-weight:300;font-size:46px;line-height:1;color:var(--text-light);letter-spacing:.5px}
  .feature-title .accent{color:var(--ink-dark)}
  .feature-subtitle{font-family:var(--heading-font);font-weight:400;font-size:19px;color:var(--ink-dark);letter-spacing:1px;margin:4px 0 14px}
  .feature-copy{font-size:12.5px;line-height:1.55;color:var(--text-light);font-style:italic}
  .feature-copy strong{font-weight:700}
  .feature-image{position:absolute;left:0;right:0;top:262px;height:222px;
    background:radial-gradient(circle at 55% 45%,#d9f0dc 0,#5fa873 12%,#1e4a2a 45%,#0b1a10 100%)}
  .feature-marker{position:absolute;left:0;top:516px;width:8px;height:66px;background:var(--band-dark)}

  /* Middle panel — contact */
  .panel--contact{background:var(--paper);border-left:1px solid #e6e6e6;border-right:1px solid #e6e6e6}
  .contact-mark{position:absolute;top:60px;left:0;right:0;display:flex;align-items:center;justify-content:center;gap:8px;
    font-family:var(--heading-font);font-weight:500;font-size:15px;color:var(--green-deep)}
  .contact-mark .dot{width:14px;height:14px;border-radius:50%;background:var(--green)}
  .name-ribbon{position:absolute;left:0;top:250px;width:360px;height:90px}
  .name-ribbon__text{position:absolute;left:0;right:0;top:32px;text-align:center;font-family:var(--heading-font);
    font-weight:400;font-size:22px;letter-spacing:2px;color:var(--text-light)}
  .contact-block{position:absolute;left:70px;right:30px;top:470px;font-size:11.5px;line-height:1.9;color:var(--text-muted)}
  .contact-heading{font-family:var(--heading-font);font-weight:500;font-size:15px;color:var(--green);letter-spacing:1px;margin-bottom:10px}
  .contact-block .gap{margin-top:14px}
  .contact-block .link{color:var(--green)}

  /* Cover panel — charcoal */
  .panel--cover{background:repeating-linear-gradient(45deg,var(--charcoal) 0 2px,var(--charcoal-deep) 2px 4px)}
  .cover-mark{position:absolute;top:92px;left:0;right:0;display:flex;align-items:center;justify-content:center;gap:10px;
    font-family:var(--heading-font);font-weight:400;font-size:18px;color:var(--text-light);letter-spacing:1px}
  .cover-mark .dot{width:22px;height:22px;border-radius:50%;border:2px solid var(--text-light)}
  .cover-image{position:absolute;left:0;right:0;top:232px;height:250px;
    background:radial-gradient(ellipse at 40% 30%,#cfcfcf 0,#6a6a6a 18%,#222 55%,#0d0d0d 100%)}
  .cover-title{position:absolute;right:0;top:260px;width:205px;height:124px;background:rgba(245,245,245,.93);
    display:flex;align-items:center;justify-content:center;padding:0 12px;
    font-family:var(--heading-font);font-weight:400;font-size:27px;letter-spacing:1px;color:var(--band-dark);text-align:center;line-height:1.15}
  .cover-tag{position:absolute;right:0;top:384px;width:205px;height:42px;background:var(--green);display:flex;align-items:center;
    padding-left:16px;gap:14px;font-family:var(--heading-font);font-size:15px;letter-spacing:1.5px;color:var(--text-light)}
  .cover-tag .ring{width:8px;height:8px;border:1.5px solid var(--text-light);border-radius:50%}
  .cover-web{position:absolute;right:22px;bottom:26px;font-family:Georgia,serif;font-size:13px;color:#d8d8d8;letter-spacing:.5px}
</style>
</head>
<body>
<main class="brochure">

  <section class="panel panel--feature">
    <div class="feature-sheet">
      <div class="feature-block feature-block--top">
        <h2 class="feature-title">LOREM<span class="accent">IPSUM</span></h2>
        <p class="feature-subtitle">LOREM IPSUM DOLOR</p>
        <p class="feature-copy"><strong>Lorem ipsum dolor sit amet,</strong> consectetur adipiscing elit. Sed at nisl feugiat, sollicitudin dui eget, porttitor odio. In a suscipit eros. In nec sem mauris. Donec diam quam, pharetra et risus quis, ornare placerat neque. Nam sit amet leo et massa accumsan dictum eget id</p>
      </div>
      <div class="feature-image" role="img" aria-label="Digital data tunnel of streaming binary code in green tones"></div>
      <span class="feature-marker"></span>
      <div class="feature-block feature-block--bottom">
        <h2 class="feature-title">LOREM</h2>
        <p class="feature-subtitle">LOREM IPSUM DOLOR</p>
        <p class="feature-copy"><strong>Lorem ipsum dolor sit amet,</strong> consectetur adipiscing elit. Sed at nisl feugiat, sollicitudin dui eget, porttitor odio. In a suscipit eros. In nec sem mauris. Donec diam quam, pharetra et risus quis, ornare placerat neque. Nam sit amet leo et massa accumsan dictum eget id</p>
      </div>
    </div>
  </section>

  <section class="panel panel--contact">
    <div class="contact-mark"><span class="dot"></span>4027 Partners</div>
    <div class="name-ribbon">
      <svg width="360" height="90" viewBox="0 0 360 90" aria-hidden="true">
        <polygon points="40,0 360,0 320,90 0,90" fill="var(--band-dark)"/>
      </svg>
      <div class="name-ribbon__text">4027 PARTNERS</div>
    </div>
    <div class="contact-block">
      <p class="contact-heading">LOREM IPSUM</p>
      <p>4027 Veltrane Partners Inc.</p>
      <p>120 Harbour Street, Suite 400</p>
      <p>Toronto, ON M5J 2L2</p>
      <p class="gap">T: +1 416 555 0187</p>
      <p>F: +1 416 555 0188</p>
      <p class="gap link">info@4027partners.com</p>
      <p class="gap">www.4027partners.com</p>
    </div>
  </section>

  <section class="panel panel--cover">
    <div class="cover-mark"><span class="dot"></span>4027 Partners</div>
    <div class="cover-image" role="img" aria-label="Server racks with streaming binary code in greyscale"></div>
    <div class="cover-title">4027 PARTNERS</div>
    <div class="cover-tag"><span class="ring"></span>LOREM IPSUM</div>
    <p class="cover-web">www.companyname.com</p>
  </section>

</main>
</body>
</html>
```